Web Design Project - Torvalen Homes

We would like you to refine our web layouts for a (1) homepage and (2) a product page (see attached files for reference).

The client is a swiss construction company, that designs, builds and sells standardized and tailored-made residential houses.

His logo is old, but not up for redesign. The only way to salvage it, is to incorporate its yellow color (as highlight) to the overall design, so as to create some brand awareness.

REQUIREMENTS FOR THE HOMEPAGE:
1. telephone number over menu
2. logo + menu with 6 categories
3. slider for showing various house types (for pics, see attachments)
4. "AKTUELL" card with yellow color (to show his most actual projects) and a strong Call For Action (what in German would be: KONTAKT AUFNEHMEN)
5. a yellow stripe for his company's slogan (Ihr Partner für individuelle und normierte Wohnbauten)
6. A left coloumn with
(a) two picture-holders under the title REFERENZEN
(b) the three supporting logos of ZIRB, KALVORTA and VB DÄMMWERK ALPEN (can be downloaded as pngs)
7. A right column with 6 headlines + texts of 3 lines each
8. a footer with the adress info

REQUIREMENTS FOR PRODUKT PAGE:
1. slider for pictures
2. info box with Call For Action for particular House-types
3. thumbnail pics under the slider for additional images of any particular house type
4. Left-side: name of house type and picture
5. Right-side: Header and blindtext for house description
6. three placeholders for 3 floor plans

NB No coding necessary. An imaginative, fresh design along the layout requirements will do.
Thanx to all

To all those who had probs with the downloading of the attached files:
we've posted a new Zip.
Have a look!
thankx

Thanks to everyone who participated.
We will be showing a selection of your designs to the client within the next couple of days.
We'll get back to you, as soon as possible.

Industry/Entity Type

Construction

Requirements
Must have
• - slider
- info box with call for action
- thumbnail pictures
- fresh look based on colors, design of elements (slider, info box), font selection

```html
<!DOCTYPE html>
<html lang="de">
<head>
<meta charset="utf-8">
<title>Torvalen Wohnbauten – Lausanne</title>
<link rel="stylesheet" href="https://fonts.googleapis.com/css2?family=Comfortaa:wght@300;400&family=Fira+Sans+Condensed:wght@300;400&family=Arimo:wght@700&display=swap">
<style>
:root{
  --yellow:#fde443;
  --yellow-deep:#f6c90f;
  --yellow-pale:#fff27a;
  --orange:#f0a400;
  --red:#e8231c;
  --ink:#2b2b2b;
  --grey:#7a7a7a;
  --line:#e2e2e2;
  --footer:#353535;
  --white:#fff;
}
*{margin:0;padding:0;box-sizing:border-box}
html,body{width:794px;height:1200px;overflow:hidden;background:var(--white)}
body{position:relative;font-family:"Comfortaa",sans-serif;color:var(--ink)}
.abs{position:absolute}

.header{left:0;top:0;width:794px;height:83px;background:var(--white)}
.brand{left:31px;top:21px;display:flex;align-items:center;gap:6px}
.brand-mark{width:12px;height:30px;background:var(--yellow-deep)}
.brand-name{font-family:"Fira Sans Condensed",sans-serif;font-weight:400;font-size:18px;line-height:1.05;color:var(--ink);letter-spacing:.5px}
.nav{left:254px;top:43px;display:flex;gap:0;font-family:"Fira Sans Condensed",sans-serif;font-weight:300;font-size:13.5px;color:var(--ink)}
.nav a{color:inherit;text-decoration:none;position:absolute;white-space:nowrap}
.nav a.active{border-bottom:1px solid var(--orange);padding-bottom:2px}
.phone{left:667px;top:43px;font-family:"Fira Sans Condensed",sans-serif;font-weight:300;font-size:14px;display:flex;align-items:center;gap:4px}

.hero{left:0;top:83px;width:794px;height:311px;background:linear-gradient(var(--yellow-deep) 0,var(--yellow) 20%,var(--yellow-pale) 100%)}
.slider{left:31px;top:96px;width:556px;height:236px;background:#f4f4f4;box-shadow:0 2px 5px rgba(0,0,0,.25)}
.slide-photo{left:31px;top:0;width:494px;height:236px;background:linear-gradient(#1d4fa0 0,#4a86d0 45%,#6f9a3e 80%,#3e6a25 100%)}
.caption{left:31px;top:173px;width:494px;height:63px;background:rgba(30,30,30,.78);color:var(--white);padding:8px 10px}
.caption h2{font-family:"Fira Sans Condensed",sans-serif;font-weight:300;font-size:15px}
.caption p{font-family:"Fira Sans Condensed",sans-serif;font-weight:300;font-size:7.5px;line-height:10px;margin-top:6px;width:470px}
.tip{left:285px;top:224px;background:#111;color:#fff;font-family:"Fira Sans Condensed",sans-serif;font-size:7.5px;padding:2px 8px}
.thumbs{left:172px;top:342px;display:flex;gap:5px}
.thumbs span{width:30px;height:34px;background:#000;border:2px solid #fff;box-shadow:0 1px 3px rgba(0,0,0,.3)}
.thumbs span.on{background:linear-gradient(#4a86d0,#6f9a3e)}

.card{left:604px;top:106px;width:159px;height:217px;background:var(--white);box-shadow:0 2px 5px rgba(0,0,0,.2)}
.card-head{height:33px;background:linear-gradient(var(--yellow-pale),var(--yellow-deep));font-family:"Arimo",sans-serif;font-size:14px;text-align:center;line-height:33px}
.spec{position:absolute;left:21px;width:125px;font-family:"Fira Sans Condensed",sans-serif;font-weight:300;font-size:9px;color:var(--grey);display:flex;justify-content:space-between;border-bottom:1px solid var(--line);padding-bottom:6px}
.cta{left:17px;top:184px;width:124px;height:32px;background:var(--red);color:#fff;font-family:"Arimo",sans-serif;font-size:9.5px;text-align:center;line-height:32px;box-shadow:0 3px 0 #9d1510}

.sec-title{font-weight:300;font-size:13px;letter-spacing:1.5px;color:var(--grey)}
.house-photo{left:31px;top:438px;width:235px;height:143px;border:3px solid #fff;outline:1px solid var(--line);background:linear-gradient(#1d4fa0 0,#4a86d0 45%,#6f9a3e 80%,#3e6a25 100%)}
.desc{left:280px;top:440px;width:440px;font-size:8.2px;line-height:16.5px;letter-spacing:.8px;color:var(--grey)}
.plan{top:624px;height:261px;background:linear-gradient(#f7f7f7,#ececec);border:1px solid var(--line)}
.plan-label{top:902px;font-weight:300;font-size:12px;letter-spacing:1.5px;color:var(--grey);text-align:center}

.footer{left:0;top:1009px;width:794px;height:191px}
.foot-title{font-size:13px;color:var(--yellow-deep);letter-spacing:1px}
.foot-text{font-size:9px;color:#e6e6e6;letter-spacing:.8px;line-height:17px}
.foot-lorem{font-family:"Fira Sans Condensed",sans-serif;font-weight:300;font-size:9.5px;color:#e6e6e6;line-height:13px}
.contact-row{display:flex;align-items:center;gap:10px;font-size:9.5px;color:#e6e6e6;letter-spacing:1px;height:22px}
.copy{left:0;top:1187px;width:650px;text-align:center;font-family:"Fira Sans Condensed",sans-serif;font-weight:300;font-size:8.5px;color:#ccc}
</style>
</head>
<body>

<header class="header abs">
  <div class="brand abs"><span class="brand-mark"></span><span class="brand-name">Torvalen<br>Wohnbauten</span></div>
  <nav class="nav abs">
    <a class="active" style="left:0">HOME</a>
    <a style="left:58px">HÄUSER</a>
    <a style="left:121px">RENOVATIONEN</a>
    <a style="left:228px">ÜBER UNS</a>
    <a style="left:302px">KONTAKT</a>
  </nav>
  <div class="phone abs">
    <svg width="12" height="16" viewBox="0 0 12 16"><path d="M3 1l2 3-1.5 2c.8 2 2 3.5 3.5 4.5L9 9l3 2-1.5 3C6 13 1 7 1 2z" fill="var(--orange)"/></svg>
    <span>044 512 38 70</span>
  </div>
</header>

<section class="hero abs">
  <div class="slider abs" style="top:13px">
    <div class="slide-photo abs" role="img" aria-label="Photo of a white two-storey house with a brown tiled roof and balcony under blue sky"></div>
    <svg class="abs" style="left:12px;top:108px" width="12" height="20"><path d="M10 2L3 10l7 8" stroke="#333" stroke-width="2.5" fill="none"/></svg>
    <svg class="abs" style="left:538px;top:108px" width="12" height="20"><path d="M2 2l7 8-7 8" stroke="var(--orange)" stroke-width="2.5" fill="none"/></svg>
    <div class="caption abs">
      <h2>Haus Typ 2</h2>
      <p>Nullam pretium auctor massa ut consequat. Etiam hendrerit iaculis mattis. Proin tincidunt gravida augue in tempor. Proin blandit, elit a consectetur tincidunt, velit quam tristique risus, eget ultrices lorem dui ut nisl.</p>
    </div>
    <div class="tip abs">Haus Typ 1</div>
  </div>
  <div class="thumbs abs" style="top:259px">
    <span class="on"></span><span></span><span></span><span></span><span></span><span></span><span></span><span></span>
  </div>
  <aside class="card abs" style="top:23px">
    <div class="card-head">LAUSANNE</div>
    <div class="spec" style="top:52px;font-weight:400">EFH</div>
    <div class="spec" style="top:77px"><span>Umbauter Raum</span><span>655 m³</span></div>
    <div class="spec" style="top:102px"><span>Brutowohnfläche</span><span>145 m²</span></div>
    <div class="spec" style="top:128px"><span>Zimmer</span><span>4½ - 5½</span></div>
    <div class="spec" style="top:153px;border:0"><span>ab CHF</span><span>xxx xxx</span></div>
    <div class="cta abs">KONTAKT AUFNEHMEN</div>
  </aside>
</section>

<h1 class="sec-title abs" style="left:31px;top:406px">LAUSANNE</h1>
<h2 class="sec-title abs" style="left:280px;top:406px">Das Klassische für das kleine Budget</h2>
<div class="house-photo abs" role="img" aria-label="Photo of the Lausanne house type, white facade, brown roof, garden lawn"></div>
<p class="desc abs">Formschöne Ansicht mit besonderer Note. Durch die flexible Raumgestal-<br>tung mag das praktische und geräumige 4½ - 5½ Zimmer-Einfamilienhaus<br>alle zu begeistern.<br>Der grosse, runde Balkon schafft zugleich Geborgenheit für den Sitplatz, der<br>Erker wertet das Wohnvergnügen um einiges auf. Nicht zuletzt geben<br>auch die beiden Querfirste dem Haus das gewisse Etwas.</p>

<div class="plan abs" style="left:12px;width:246px" role="img" aria-label="Floor plan of the basement"></div>
<div class="plan abs" style="left:273px;width:245px" role="img" aria-label="Floor plan of the ground floor"></div>
<div class="plan abs" style="left:538px;width:231px" role="img" aria-label="Floor plan of the upper floor"></div>
<div class="plan-label abs" style="left:12px;width:258px">Untergeschoss</div>
<div class="plan-label abs" style="left:273px;width:262px">Erdgeschoss</div>
<div class="plan-label abs" style="left:538px;width:231px">Obergeschoss</div>

<footer class="footer abs">
  <svg class="abs" style="left:0;top:0" width="794" height="191"><path d="M0 48C120 48 230 46 300 30C360 15 420 2 500 4C580 6 640 30 690 42C730 48 770 48 794 48V191H0Z" fill="var(--footer)"/></svg>
  <div class="foot-title abs" style="left:351px;top:20px">Über Uns</div>
  <div class="foot-title abs" style="left:85px;top:64px">Adresse</div>
  <div class="foot-text abs" style="left:31px;top:86px">Torvalen Wohnbauten GmbH<br>Fam. Brenner<br>Weidenstrasse 14<br>CH-8412 Arnsried</div>
  <p class="foot-lorem abs" style="left:286px;top:67px;width:270px">Lorem ipsum dolor sit amet, consectetur adipiscing elit. Pellentesque a purus leo. Sed pellentesque, lacus eu congue adipiscing, neque quam porta lorem, at blandit lorem sapien sed nulla. Duis tempor, nisl eget lacinia. Lorem ipsum dolor sit amet, consectetur adipiscing elit. Pellentesque a purus leo. Sed pellentesque, lacus eu <span style="color:var(--yellow-deep);text-decoration:underline">mehr</span></p>
  <div class="foot-title abs" style="left:665px;top:64px">Kontakt</div>
  <div class="abs" style="left:609px;top:84px">
    <div class="contact-row"><svg width="14" height="16" viewBox="0 0 12 16"><path d="M3 1l2 3-1.5 2c.8 2 2 3.5 3.5 4.5L9 9l3 2-1.5 3C6 13 1 7 1 2z" fill="#ddd"/></svg>044 512 38 70</div>
    <div class="contact-row"><svg width="14" height="14"><rect x="3" y="1" width="8" height="4" fill="#ddd"/><rect x="1" y="5" width="12" height="6" rx="1" fill="#ddd"/><rect x="3" y="10" width="8" height="3" fill="#aaa"/></svg>044 512 38 71</div>
    <div class="contact-row" style="font-size:9px;letter-spacing:0;text-decoration:underline"><svg width="14" height="10"><rect x=".5" y=".5" width="13" height="9" fill="none" stroke="#ddd"/><path d="M.5 .5L7 6l6.5-5.5" fill="none" stroke="#ddd"/></svg>info@torvalen-wohnbauten.ch</div>
  </div>
  <svg class="abs" style="left:738px;top:167px" width="24" height="24"><circle cx="12" cy="12" r="11" fill="var(--orange)" stroke="#fff" stroke-width="1.5"/><path d="M12 6l-5 5h3v6h4v-6h3z" fill="#fff"/></svg>
</footer>
<div class="copy abs">Copyright © 2013 - Kernwerk Studio -</div>

</body>
</html>
```